Social Search engine to end child poverty

Velquor.org is a search engine based in Houston, that donates 50% or more of its profits to nonprofit organizations that focus on ending child poverty. We consider itself a social business, claims to support full financial transparency,protect the privacy of its users;

Velquor shows advertisements next to its search results, and is paid by partners every time a user is directed to an advertiser via a sponsored link.
We are committed to becoming a privacy friendly search engine. Searches will be encrypted, not stored permanently, and data will not not sold to third party advertisers.
Like www.parvink.org Every search done by website visitor will generate a TUPRAK that will be stored in his wallet. Then the visitor can donate these TUPRAKS to The idea behind is evry donation will put a SMILE back on a child face

The search engine will partner with foundations/associations/NGOs that will be able to propose crowdfunding campaigns on the landing page

The beta test will be done with african children. So the landing page should show faces of happiness, joy, children

Please find attached inspirational ideas in the PDF file

Target Market(s)

NGO, Foundation, association, donators based in USA

Industry/Entity Type

Charity

Number of Pages Required

5+ page

Colors
33a6d7
fbed22
f04a50
a54499
f78d1f
add136

Requirements
Must have
• Landing page
• 0- Number of TUPRAKS collected worlwide/number of projects funded
• 1- explaining how it works and
• 2- samples of fundable projects
• 3- Become partner
• Search results
• 1- Sponsored results should be differentiated
• 2- The search page should advertise initiative pr people that acts in the world to end child poverty.
• 3 It should also provide quizzes with some metrics/figures on child poverty
• Under the search engine bar should be "News" "Videos

```html
<!DOCTYPE html>
<html lang="en">
<head>
<meta charset="utf-8">
<title>Velquor.org – Search results</title>
<link href="https://fonts.googleapis.com/css2?family=Lato:wght@400;700&display=swap" rel="stylesheet">
<style>
:root{
  --blue:#33a6d7;
  --link:#4b4fc4;
  --green:#3f9b3a;
  --text:#555a60;
  --muted:#9aa0a6;
  --line:#e6e8eb;
  --yellow:#fbed22;
  --orange:#f78d1f;
  --bg:#ffffff;
}
*{box-sizing:border-box;margin:0;padding:0}
html,body{width:724px;height:1200px;overflow:hidden;background:var(--bg);font-family:'Lato',sans-serif;color:var(--text)}
.page{position:relative;width:724px;height:1200px}
.abs{position:absolute}
.site-header{left:0;top:0;width:724px;height:54px;border-bottom:1px solid var(--line)}
.brand{left:20px;top:14px;font-size:21px;font-weight:700;color:var(--blue)}
.search-box{left:125px;top:11px;width:348px;height:34px;border:1px solid #dcdfe3;border-radius:17px;box-shadow:0 1px 3px rgba(0,0,0,.08);font-size:10px;color:var(--muted);padding:11px 16px}
.search-box svg{position:absolute;right:14px;top:10px}
.wallet{left:628px;top:19px;display:flex;align-items:center;gap:5px;font-size:11px;font-weight:700;color:var(--text)}
.coin{width:14px;height:14px;border-radius:50%;background:var(--orange)}
.menu{left:690px;top:20px}
.tabs{left:133px;top:62px;width:470px;height:16px;font-size:9px;color:var(--muted);border-bottom:1px solid var(--line)}
.tabs span{margin-right:14px}
.tabs .active{color:var(--link);font-weight:700;border-bottom:2px solid var(--link);padding-bottom:3px}
.tabs .tools{position:absolute;right:0;top:0}
.tabs .tools span{margin:0 0 0 14px}
.count{left:133px;top:86px;font-size:7.5px;color:var(--muted)}
.result{left:133px;width:282px}
.result h3{font-size:13.5px;font-weight:700;color:var(--link);line-height:16px}
.ad-tag{display:inline-block;font-size:7px;font-weight:400;color:var(--muted);border:1px solid #d6d8dc;border-radius:2px;padding:0 3px;margin-left:6px;vertical-align:middle}
.url{font-size:7.5px;color:var(--green);line-height:11px}
.snippet{font-size:7.5px;line-height:10px;color:var(--text)}
.sitelinks{left:146px;top:190px;width:260px;display:grid;grid-template-columns:1fr 1fr;row-gap:10px;column-gap:20px}
.sitelinks b{display:block;font-size:10px;font-weight:400;color:var(--link);margin-bottom:2px}
.sitelinks p{font-size:7px;line-height:9px}
.side-ad{left:470px;width:135px}
.side-ad h4{font-size:9px;font-weight:700;color:var(--link);line-height:12px}
.side-ad .url{font-size:7px}
.side-ad p{font-size:7px;line-height:9px}
.news-title{left:133px;top:632px;font-size:12px;font-weight:700;color:var(--text)}
.news-row{left:133px;top:651px;display:flex;gap:6px}
.news-card{width:92px;height:106px;border:1px solid var(--line);border-radius:3px;overflow:hidden;font-size:7px}
.news-photo{height:48px;background:linear-gradient(135deg,#b3473a,#e3a84a 60%,#6b4a3a)}
.news-card b{display:block;font-weight:400;color:var(--link);padding:5px 6px 0;line-height:9px;height:30px}
.news-card small{display:flex;justify-content:space-between;padding:6px 6px 0;font-size:6px;color:var(--muted)}
.news-next{left:418px;top:688px}
.more-news{left:138px;top:763px;font-size:7px;color:var(--link)}
.related{left:133px;top:1020px;width:282px}
.related h5{font-size:7px;font-weight:400;color:var(--muted);margin-bottom:6px}
.related div{display:grid;grid-template-columns:repeat(4,1fr);row-gap:6px;font-size:7px;color:var(--link)}
.pager{left:220px;top:1096px;display:flex;gap:13px;font-size:8px;color:var(--link)}
.pager .current{color:var(--text);font-weight:700}
.site-footer{left:0;top:1156px;width:724px;height:44px;border-top:1px solid var(--line);font-size:7px;color:var(--muted)}
.site-footer .copy{position:absolute;left:20px;top:16px}
.site-footer nav{position:absolute;left:388px;top:16px;display:flex;gap:14px}
.site-footer .social{position:absolute;right:20px;top:14px;display:flex;gap:9px}
.site-footer .social span{width:8px;height:8px;border-radius:50%;background:#b9bec4}
</style>
</head>
<body>
<div class="page">
  <header class="site-header abs">
    <div class="brand abs">Velquor.org</div>
    <div class="search-box abs">Search the web to share smiles...
      <svg width="13" height="13" viewBox="0 0 13 13"><circle cx="5.5" cy="5.5" r="4" fill="none" stroke="#666" stroke-width="1.4"/><path d="M8.5 8.5l3.5 3.5" stroke="#666" stroke-width="1.4"/></svg>
    </div>
    <div class="wallet abs"><span class="coin"></span>13</div>
    <svg class="menu abs" width="14" height="12" viewBox="0 0 14 12"><path d="M0 1h14M0 6h14M0 11h14" stroke="#555" stroke-width="1.6"/></svg>
  </header>

  <nav class="tabs abs"><span class="active">Web</span><span>Images</span><span>Videos</span><span>News</span><span>Maps</span><span>Shopping</span>
    <div class="tools"><span>Filters</span><span>Settings</span></div></nav>
  <div class="count abs">About 24,600,000 results</div>

  <article class="result abs" style="top:126px">
    <h3>Search Result Sentence - Visit Now <span class="ad-tag">Ad</span></h3>
    <div class="url">www.examplewebsite.com</div>
    <p class="snippet">Lorem ipsum dolor sit amet, consectetur adipiscing elit. Pellentesque vestibulum egestas felis et elementum lorem tempor sed. In hac ultricies, odio lacus a euismod.</p>
  </article>
  <div class="sitelinks abs">
    <div><b>Category 1</b><p>Lorem ipsum dolor sit amet, consectetur adipiscing elit. Sed erat tristique lorem eget molestie lacus.</p></div>
    <div><b>Category 2</b><p>Lorem ipsum dolor sit amet, consectetur adipiscing elit. Sed erat tristique lorem eget molestie lacus.</p></div>
    <div><b>Category 3</b><p>Lorem ipsum dolor sit amet, consectetur adipiscing elit. Sed erat tristique lorem eget molestie lacus.</p></div>
    <div><b>Category 4</b><p>Lorem ipsum dolor sit amet, consectetur adipiscing elit. Sed erat tristique lorem eget molestie lacus.</p></div>
  </div>

  <article class="result abs" style="top:318px"><h3>Search Result Sentence - Visit Now</h3><div class="url">www.examplewebsite.com</div><p class="snippet">Lorem ipsum dolor sit amet, consectetur adipiscing elit. Pellentesque vestibulum egestas felis et elementum lorem tempor sed. In hac ultricies, odio lacus a euismod.</p></article>
  <article class="result abs" style="top:391px"><h3>Search Result Sentence - Visit Now</h3><div class="url">www.examplewebsite.com</div><p class="snippet">Lorem ipsum dolor sit amet, consectetur adipiscing elit. Pellentesque vestibulum egestas felis et elementum lorem tempor sed. In hac ultricies, odio lacus a euismod.</p></article>
  <article class="result abs" style="top:470px"><h3>Search Result Sentence - Visit Now</h3><div class="url">www.examplewebsite.com</div><p class="snippet">Lorem ipsum dolor sit amet, consectetur adipiscing elit. Pellentesque vestibulum egestas felis et elementum lorem tempor sed. In hac ultricies, odio lacus a euismod.</p></article>
  <article class="result abs" style="top:547px"><h3>Search Result Sentence - Visit Now</h3><div class="url">www.examplewebsite.com</div><p class="snippet">Lorem ipsum dolor sit amet, consectetur adipiscing elit. Pellentesque vestibulum egestas felis et elementum lorem tempor sed. In hac ultricies, odio lacus a euismod.</p></article>

  <aside class="side-ad abs" style="top:124px"><h4>Advertised Search <span class="ad-tag">Ad</span></h4><div class="url">www.examplewebsite.com</div><p>Lorem ipsum dolor sit amet, consectetur adipiscing elit sed.</p></aside>
  <aside class="side-ad abs" style="top:194px"><h4>Advertised Search <span class="ad-tag">Ad</span></h4><div class="url">www.examplewebsite.com</div><p>Lorem ipsum dolor sit amet, consectetur adipiscing elit sed.</p></aside>

  <h2 class="news-title abs">Recent News</h2>
  <div class="news-row abs">
    <div class="news-card"><div class="news-photo" role="img" aria-label="Photo of smiling children for a news video"></div><b>News video of the day example</b><small><span>Velquor</span><span>3 hrs</span></small></div>
    <div class="news-card"><div class="news-photo" role="img" aria-label="Photo of smiling children for a news video"></div><b>News video of the day example</b><small><span>Velquor</span><span>3 hrs</span></small></div>
    <div class="news-card"><div class="news-photo" role="img" aria-label="Photo of smiling children for a news video"></div><b>News video of the day example</b><small><span>Velquor</span><span>3 hrs</span></small></div>
  </div>
  <svg class="news-next abs" width="8" height="12" viewBox="0 0 8 12"><path d="M2 1l5 5-5 5" fill="none" stroke="#777" stroke-width="1.5"/></svg>
  <div class="more-news abs">See more news &rsaquo;</div>

  <article class="result abs" style="top:788px"><h3>Search Result Sentence - Visit Now</h3><div class="url">www.examplewebsite.com</div><p class="snippet">Lorem ipsum dolor sit amet, consectetur adipiscing elit. Pellentesque vestibulum egestas felis et elementum lorem tempor sed. In hac ultricies, odio lacus a euismod.</p></article>
  <article class="result abs" style="top:865px"><h3>Search Result Sentence - Visit Now</h3><div class="url">www.examplewebsite.com</div><p class="snippet">Lorem ipsum dolor sit amet, consectetur adipiscing elit. Pellentesque vestibulum egestas felis et elementum lorem tempor sed. In hac ultricies, odio lacus a euismod.</p></article>
  <article class="result abs" style="top:940px"><h3>Search Result Sentence - Visit Now</h3><div class="url">www.examplewebsite.com</div><p class="snippet">Lorem ipsum dolor sit amet, consectetur adipiscing elit. Pellentesque vestibulum egestas felis et elementum lorem tempor sed. In hac ultricies, odio lacus a euismod.</p></article>

  <section class="related abs">
    <h5>Searches related to example</h5>
    <div><span>Lorem ipsum</span><span>dolor sit amet</span><span>consectetur adipiscing</span><span>Pellentesque vestibulum</span>
    <span>egestas felis</span><span>elementum lorem tempor</span><span>in hac ultricies euismod</span><span>odio a viverra</span></div>
  </section>

  <nav class="pager abs"><span class="current">1</span><span>2</span><span>3</span><span>4</span><span>5</span><span>6</span><span>&rsaquo;</span></nav>

  <footer class="site-footer abs">
    <span class="copy">© 2024 Velquor.org</span>
    <nav><span>Privacy policy</span><span>Terms of use</span><span>About Us</span><span>Become a partner</span></nav>
    <div class="social"><span></span><span></span><span></span></div>
  </footer>
</div>
</body>
</html>
```